GUARANTEED WordPress design needed for a sassy, confident charisma coach!

We need a website design for Marla Penrick's brand new, responsive, Wordpress website.
Marla is a trainer / coach who teaches people how to be more charismatic and runs events, publishes video courses and has an ongoing video blog. Her old website is here: www.marlapenrick.co.uk ... but it's now time to have a much better site!
We have a strong idea about the technical components of the website, but we need a designer's eye to create a great style for the site (and provide layered PSD files which our developers will then convert to HTML and CSS).
Marla's brand is sassy, brave, warm and confident. The videos on her existing site give quite a good feel for her personality. We need a clean, stylish and compelling page that isn't too corporate and captures her personality. Every element needs to feel coherent, from fonts and headings to colours and spacing.
The following sites are not exactly what Marla wants (and certainly aren't right in terms of colours) but they give you an idea of the kind of people she is competing against and the area she is operating in:
http://www.tessa-broughley.example/
http://rowanfelsby.example/
Ideally, you will have done something similar and be able to key in on exactly the kind of thing we want: we're not looking to reinvent the wheel. Hopefully you won't mind tweaking a few things if you are close to what we need.
More detail is provided in the word document attached. But in a nutshell we need: a banner, footer, sign-up strap, menu bar, signature and 4 different basic page types. We want bursts of bright colours, contrasted with black and white if possible - sorry we can't be more specific than that...
The word doc also contains some amateur mock-ups as well (the images are also just mockups at this stage) - but although these give a general sense of the structure what we are looking for, we are clearly not designers...so please help! We need a designer's touch!
Kind regards,
Corin
PS The layered PSD versions of the mockup files are available on Cloudvantre: https://files.cloudvantre.example/sh/k72pqa4w1zbtmrd/QXvenlr8Ty3PwMiU6Hs2kYfDb?dl=0
Target Market(s)
Entrepreneurs who need to sell themselves.
Number of Pages Required
4 page

```html
<!DOCTYPE html>
<html lang="en">
<head>
<meta charset="utf-8">
<title>Marla Penrick – Charisma Coach</title>
<link rel="stylesheet" href="https://fonts.googleapis.com/css2?family=Roboto+Condensed:wght@300;400;700&family=Roboto:wght@400&family=Open+Sans:wght@700&display=swap">
<style>
:root{
  --red:#d0112b;
  --red-active:#df3f22;
  --wine:#6d0817;
  --ink:#222;
  --text:#444;
  --muted:#6b6b6b;
  --page:#e4e4e4;
  --white:#fff;
  --sky-top:#c6d6e2;
  --sky-bottom:#dce5ec;
  --tag-blue:#3b6fd6;
  --tag-pink:#d8336e;
  --tw:#2fa3dc;
  --tb:#36465d;
  --fb:#3a5a9a;
  --mail:#7f939d;
  --print:#8fa0a8;
  --more:#f26a4e;
}
*{box-sizing:border-box;margin:0;padding:0}
html,body{width:1197px;height:1200px;overflow:hidden;background:var(--page)}
body{position:relative;font-family:"Roboto Condensed",sans-serif;color:var(--ink)}
.abs{position:absolute}

/* header */
.site-header{position:absolute;left:0;top:0;width:1197px;height:100px;background:var(--white)}
.brand{position:absolute;left:115px;top:32px;font-family:"Roboto Condensed",sans-serif;font-weight:700;font-size:30px;color:var(--ink);line-height:36px}
.social{position:absolute;left:572px;top:36px;display:flex;gap:9px}
.social span{width:28px;height:28px;border-radius:50%;background:#3a3a3a;display:block}
.search{position:absolute;left:844px;top:32px;width:245px;height:39px;border:3px solid var(--ink);font-family:Roboto,sans-serif;font-size:13px;color:#555;padding:0 0 0 16px;line-height:33px}
.search svg{position:absolute;right:8px;top:7px}

/* nav */
.main-nav{position:absolute;left:0;top:100px;width:1197px;height:43px;background:var(--red)}
.main-nav ul{list-style:none;position:absolute;left:113px;top:0;display:flex;border-right:1px solid #e2515f}
.main-nav li{height:43px;line-height:43px;text-align:center;color:var(--white);font-weight:700;font-size:15px;border-left:1px solid #e2515f}
.main-nav li.active{background:var(--red-active)}

/* hero */
.hero{position:absolute;left:0;top:143px;width:1197px;height:347px;background:linear-gradient(180deg,var(--sky-top),var(--sky-bottom))}
.hero-portrait{position:absolute;left:782px;top:0;width:220px;height:347px;background:linear-gradient(180deg,rgba(224,70,80,.18),rgba(215,30,50,.28))}
.hero-title{position:absolute;left:149px;top:68px;width:572px;text-align:center;font-weight:700;font-size:30px;color:#111}
.hero-text{position:absolute;left:149px;top:112px;width:572px;text-align:center;font-size:12px;line-height:20px;color:#222}
.btn-hero{position:absolute;left:362px;top:203px;width:146px;height:40px;background:var(--red);border:2px solid var(--white);color:var(--white);font-weight:700;font-size:15px;line-height:36px;text-align:center}

/* posts */
.post-card{position:absolute;left:113px;width:644px;background:var(--white)}
.post-media{position:absolute;left:33px;top:34px;width:578px}
.tag{position:absolute;left:0;top:32px;height:26px;width:99px;color:var(--white);font-weight:700;font-size:11px;line-height:26px;text-align:center}
.post-title{position:absolute;left:33px;top:280px;width:578px;font-weight:700;font-size:28px;line-height:33px;color:var(--red)}
.post-body{position:absolute;left:33px;top:358px;width:578px;font-weight:300;font-size:10.2px;line-height:20px;color:var(--text)}
.post-body p+p{margin-top:20px}
.post-meta{position:absolute;left:33px;top:541px;width:578px;border-top:1px solid #ccc;height:60px;font-family:Roboto,sans-serif;font-size:11px;color:#444}
.meta-item{position:absolute;top:20px;display:flex;align-items:center;gap:8px}
.meta-item.author{font-family:"Roboto Condensed",sans-serif;font-weight:700;color:var(--red);font-size:11px}

.share-bar{position:absolute;left:74px;width:39px}
.share-bar div{height:43.5px;position:relative;display:flex;justify-content:center;padding-top:10px}
.share-bar small{position:absolute;bottom:2px;left:0;width:100%;text-align:center;color:var(--white);font-family:Roboto,sans-serif;font-size:7.5px}
.share-bar .dot{width:16px;height:16px;border-radius:3px;background:rgba(255,255,255,.9)}

/* sidebar */
.sidebar{position:absolute;left:782px;top:523px;width:309px;height:700px;background:var(--white)}
.ad-space{position:absolute;left:28px;top:28px;width:252px;height:213px;background:var(--wine);color:var(--white);font-family:"Open Sans",sans-serif;font-weight:700;font-size:45px;line-height:40px;text-align:center;padding-top:26px}
.rule{position:absolute;left:0;width:309px;height:1px;background:#d6d6d6}
.widget-title{position:absolute;left:29px;font-weight:700;font-size:23px;color:var(--ink)}
.widget-text{position:absolute;left:29px;top:336px;width:260px;font-weight:300;font-size:10px;line-height:20px;color:var(--text)}
.field{position:absolute;left:29px;width:249px;height:31px;border:2px solid var(--ink);font-family:Roboto,sans-serif;font-size:12px;color:#444;line-height:27px;padding-left:15px}
.btn-sub{position:absolute;left:29px;top:461px;width:93px;height:27px;background:var(--red);color:var(--white);font-weight:700;font-size:11px;line-height:27px;text-align:center}
.story-thumb{position:absolute;left:29px;top:589px;width:102px;height:77px;background:linear-gradient(180deg,#b9c9d6,#d8cdb8)}
.story-text{position:absolute;left:143px;top:593px;width:140px;font-weight:700;font-size:12px;line-height:19px;color:var(--ink)}
</style>
</head>
<body>

<header class="site-header">
  <div class="brand">Marla Penrick</div>
  <div class="social" aria-label="Social profiles">
    <span></span><span></span><span></span><span></span><span></span><span></span><span></span>
  </div>
  <div class="search">Enter your keyword...
    <svg width="20" height="20" viewBox="0 0 20 20" fill="none" stroke="#222" stroke-width="2.2"><circle cx="8" cy="8" r="6"/><line x1="12.5" y1="12.5" x2="18" y2="18"/></svg>
  </div>
</header>

<nav class="main-nav">
  <ul>
    <li class="active" style="width:142px">HOME</li>
    <li style="width:167px">EVENTS</li>
    <li style="width:167px">WORK WITH ME</li>
    <li style="width:168px">CORPORATE</li>
    <li style="width:167px">ABOUT</li>
    <li style="width:167px">CONTACT</li>
  </ul>
</nav>

<section class="hero" role="img" aria-label="Pale sky with a modern white building rising behind the headline">
  <div class="hero-portrait" role="img" aria-label="Portrait of Marla in a red dress, hands on hips"></div>
  <h1 class="hero-title">Attract, connect, influence!</h1>
  <p class="hero-text">Chapter too parties its letters nor. Cheerful but whatever ladyship disposed yet judgment. Lasted answer oppose to ye months no esteem. Branched is on an ecstatic directly it. Put off continue you denoting returned juvenile. Looked person sister result mr to. Replied demands charmed do viewing ye colonel to so. Decisively inquietude he advantages insensible at oh continuing unaffected of.</p>
  <div class="btn-hero">CONTACT MARLA</div>
</section>

<!-- share bar, first post -->
<div class="share-bar" style="top:490px">
  <div style="background:var(--tw)"><span class="dot"></span><small>15.7K</small></div>
  <div style="background:var(--tb)"><span class="dot"></span></div>
  <div style="background:var(--fb)"><span class="dot"></span><small>123K</small></div>
  <div style="background:var(--mail)"><svg width="18" height="13" viewBox="0 0 18 13" fill="none" stroke="#fff" stroke-width="1.6"><rect x="1" y="1" width="16" height="11"/><polyline points="1,1 9,7 17,1"/></svg></div>
  <div style="background:var(--print)"><svg width="18" height="16" viewBox="0 0 18 16" fill="none" stroke="#fff" stroke-width="1.6"><rect x="5" y="1" width="8" height="4"/><rect x="1" y="5" width="16" height="7"/><rect x="5" y="10" width="8" height="5" fill="var(--print)"/></svg></div>
  <div style="background:var(--more)"><svg width="16" height="16" viewBox="0 0 16 16" stroke="#fff" stroke-width="3"><line x1="8" y1="1" x2="8" y2="15"/><line x1="1" y1="8" x2="15" y2="8"/></svg><small>2.6M</small></div>
</div>

<article class="post-card" style="top:456px;height:597px">
  <div class="post-media" role="img" aria-label="Wall covered with open book pages" style="height:233px;background:linear-gradient(135deg,#c9b3a0,#a98a78 55%,#c7ad98)">
    <span class="tag" style="background:var(--tag-blue)">MOTIVATION</span>
  </div>
  <h2 class="post-title">Breakfast agreeable incommode departure it an. By ignorant at on wondered relation</h2>
  <div class="post-body">
    <p>Exposed neither pressed so cottage as proceed at offices. Nay they gone sir game four. Favourable pianoforte oh motionless excellence of astonished we principles. Warrant present garrets limited cordial in inquiry to. Supported me sweetness behaviour shameless excellent so arranging.</p>
    <p>Remain lively hardly needed at do by. Two you fat downs fanny three. True mr gone most at. Dare as name just when with it body. Travelling inquietude she increasing off impossible the. Cottage be noisier looking to we promise on. Disposal to kindness appetite diverted learning of on raptures. Betrayed any may returned now dashwood formerly. Balls way delay shy boy man views.</p>
  </div>
  <div class="post-meta">
    <span class="meta-item author" style="left:0"><svg width="20" height="20" viewBox="0 0 20 20" fill="#aaa"><circle cx="10" cy="6" r="5"/><path d="M0 20c0-6 4-8 10-8s10 2 10 8z"/></svg>By: Marla Penrick</span>
    <span class="meta-item" style="left:136px"><svg width="18" height="18" viewBox="0 0 18 18" fill="#aaa"><rect x="0" y="3" width="18" height="15"/><rect x="3" y="0" width="3" height="5"/><rect x="12" y="0" width="3" height="5"/></svg>12.12.2014</span>
    <span class="meta-item" style="left:249px"><svg width="20" height="16" viewBox="0 0 20 16" fill="#aaa"><ellipse cx="10" cy="7" rx="10" ry="7"/><path d="M3 11l-2 5 6-3z"/></svg>11 comments</span>
    <span class="meta-item" style="left:376px"><svg width="20" height="18" viewBox="0 0 20 18" fill="#aaa"><path d="M10 18L1.5 9.5A5 5 0 0 1 10 3a5 5 0 0 1 8.5 6.5z"/></svg>5 favorites</span>
    <span class="meta-item" style="left:491px"><svg width="20" height="12" viewBox="0 0 20 12"><ellipse cx="10" cy="6" rx="9.5" ry="5.5" fill="#aaa"/><circle cx="10" cy="6" r="3" fill="#fff"/><circle cx="10" cy="6" r="1.5" fill="#aaa"/></svg>1.128 views</span>
  </div>
</article>

<!-- second post -->
<div class="share-bar" style="top:1103px">
  <div style="background:var(--tw)"><span class="dot"></span><small>15.7K</small></div>
  <div style="background:var(--tb)"><span class="dot"></span></div>
  <div style="background:var(--fb)"><span class="dot"></span></div>
</div>
<article class="post-card" style="top:1070px;height:200px">
  <div class="post-media" role="img" aria-label="Blurred black and white photo of cyclists in motion" style="height:120px;background:linear-gradient(90deg,#7a7a7a,#bdbdbd 40%,#6d6d6d 75%,#9c9c9c)">
    <span class="tag" style="background:var(--tag-pink)">SCIENCE</span>
  </div>
</article>

<aside class="sidebar">
  <div class="ad-space">This is<br>an<br>ad<br>space</div>
  <div class="rule" style="top:268px"></div>
  <h3 class="widget-title" style="top:296px">Unlock your superpowers!</h3>
  <p class="widget-text">Learn how to unlock the superpower* of your charisma and win all the business. You want with this FREE training.</p>
  <div class="field" style="top:377px">First Name</div>
  <div class="field" style="top:418px">Email</div>
  <div class="btn-sub">YES, PLEASE!</div>
  <div class="rule" style="top:518px"></div>
  <h3 class="widget-title" style="top:545px">Top stories of the week</h3>
  <div class="story-thumb" role="img" aria-label="Lifeguard hut on a sandy beach"></div>
  <p class="story-text">By ignorant at on wondered relation. Enough at tastes really so cousin am</p>
</aside>

</body>
</html>
```